Exceptional Properties Flyer

I need a flyer template that I can re-use for high-end home listings over $1m in price. 11 X 17 horizontal folded to open wtih front photo shot large on front with short descriptionon areas, room for my photo, logo, contact info & property address then photo slots inside all pagers with room for copy to be plugged in. 3-4 photo spots per page at various sizes but room for bullet point descriptions on pages somewhere. Back of flyer larger photo slot and 2-3 smaller spots below with room for my photo and contact info
My contact info:
Maelle Hutchins
Real Estate Broker
Pelham Group Real Estate
Direct 206.555.0174
Email: maelle.hutchin@norvalehomes.com

```html
<!DOCTYPE html>
<html lang="en">
<head>
<meta charset="utf-8">
<title>Exceptional Properties Flyer</title>
<link href="https://fonts.googleapis.com/css2?family=Montserrat:wght@400;500;600;700&family=Yellowtail&display=swap" rel="stylesheet">
<style>
  :root{
    --stage:#3b3b3d;
    --stage-edge:#2c2c2e;
    --gold:#c9a81f;
    --gold-light:#dcc02f;
    --gold-deep:#a8890f;
    --ink:#0c0c0c;
    --paper:#ffffff;
    --label:#ffffff;
    --body-dark:#2a2a2a;
  }
  *{box-sizing:border-box;margin:0;padding:0}
  html,body{width:1200px;height:1200px;overflow:hidden}
  body{
    background:radial-gradient(ellipse at center,var(--stage) 0%,var(--stage-edge) 100%);
    font-family:"Montserrat",Arial,sans-serif;
    position:relative;
  }
  .side-label{position:absolute;color:var(--label);font-weight:700;font-size:13px;transform:translateX(-50%)}
  .side-label--back{left:120px;top:364px}
  .side-label--front{left:1041px;top:364px}
  .side-label--inside{left:120px;top:859px}

  .spread{position:absolute;left:162px;width:847px;height:548px;overflow:hidden;background:var(--paper);box-shadow:0 4px 18px rgba(0,0,0,.45)}
  .spread--outside{top:43px}
  .spread--inside{top:597px}
  .spread svg.art{position:absolute;left:0;top:0;width:847px;height:548px}
  .fold{position:absolute;left:423px;top:0;width:1px;height:548px;background:rgba(0,0,0,.18)}

  .abs{position:absolute}
  .brand{font-weight:700;font-size:19px;color:var(--ink);letter-spacing:-.2px;white-space:nowrap;text-align:right}
  .brand--front{right:26px;top:50px}
  .brand--inside{right:28px;top:40px}

  /* back cover */
  .team-tag{left:119px;top:462px;width:124px;height:51px;color:#fff;text-align:right;padding:8px 24px 0 0;line-height:1.1}
  .team-tag__name{color:var(--gold-light);font-weight:700;font-size:11.5px;display:block;white-space:nowrap}
  .team-tag__sub{font-size:11px;display:block}
  .agent-card{text-align:right;color:var(--ink)}
  .agent-card__name{font-family:"Yellowtail",cursive;font-size:26px;line-height:1;white-space:nowrap}
  .agent-card__title{font-style:italic;font-weight:500;font-size:10.5px;margin-top:3px}
  .agent-card__phone{font-weight:700;font-size:20px;margin-top:3px;letter-spacing:.2px}
  .agent-card__email{font-size:9.6px;margin-top:1px;white-space:nowrap}
  .agent-card--back{right:445px;top:446px}
  .agent-card--front{right:25px;top:460px}
  .agent-card--front .agent-card__name{font-size:23px}
  .agent-card--front .agent-card__title{font-size:9.5px}
  .agent-card--front .agent-card__phone{font-size:20px}
  .agent-card--front .agent-card__email{font-size:9.2px}

  .front-desc{left:445px;top:443px;width:205px;color:var(--ink)}
  .heading-block{font-weight:700;font-size:15.5px;line-height:1.08;text-transform:uppercase}
  .front-desc p{font-size:9px;line-height:1.27;margin-top:4px;color:var(--body-dark)}

  /* inside */
  .page-head{left:26px;top:38px;color:#fff;font-weight:700;font-size:30px;line-height:1.0;text-transform:uppercase}
  .page-intro{left:26px;top:104px;width:262px;color:#fff;font-size:9.4px;line-height:1.45}
  .side-column{left:299px;top:25px;width:114px;color:#fff;font-size:7.1px;line-height:1.24}
  .subhead{left:26px;top:362px;font-weight:700;font-size:16px;color:var(--ink);text-transform:uppercase}
  .subhead-intro{left:26px;top:383px;width:390px;font-size:9.3px;line-height:1.3;color:var(--body-dark)}
  .body-column{top:416px;width:192px;font-size:7.6px;line-height:1.3;color:var(--body-dark)}
  .body-column--one{left:26px}
  .body-column--two{left:231px}

  .bullets-head{left:436px;top:27px;color:#fff;font-weight:700;font-size:16.5px;line-height:1.1;text-transform:uppercase}
  .bullet-list{left:436px;top:68px;width:180px;color:#fff;font-weight:600;font-size:10.6px;line-height:1.25;list-style:none}
  .bullet-list li{position:relative;padding-left:13px;margin-bottom:7px}
  .bullet-list li::before{content:"";position:absolute;left:1px;top:5px;width:3px;height:3px;border-radius:50%;background:#fff}
  .side-note{left:641px;top:134px;width:184px;color:#fff;font-size:7.6px;line-height:1.3}
  .listing{top:384px;width:118px;color:var(--ink)}
  .listing .heading-block{font-size:12.8px}
  .listing p{font-size:7.5px;line-height:1.3;margin-top:5px;color:var(--body-dark)}
  .listing--one{left:436px}
  .listing--two{left:573px}
  .listing--three{left:710px}
</style>
</head>
<body>

<span class="side-label side-label--back">Back</span>
<span class="side-label side-label--front">Front</span>
<span class="side-label side-label--inside">Inside</span>

<!-- Outside spread: back cover (left) and front cover (right) -->
<section class="spread spread--outside">
  <svg class="art" viewBox="0 0 847 548">
    <defs>
      <linearGradient id="goldPanel" x1="0" y1="0" x2="0" y2="1">
        <stop offset="0" stop-color="#d9bd2c"/>
        <stop offset=".55" stop-color="#cdad22"/>
        <stop offset="1" stop-color="#a98a12"/>
      </linearGradient>
      <linearGradient id="exteriorTone" x1="0" y1="0" x2="0" y2="1">
        <stop offset="0" stop-color="#9fb28a"/>
        <stop offset=".35" stop-color="#6d7566"/>
        <stop offset=".75" stop-color="#5c6556"/>
        <stop offset="1" stop-color="#4d7a36"/>
      </linearGradient>
      <radialGradient id="roomWarm" cx=".5" cy=".5" r=".6">
        <stop offset="0" stop-color="#e6d3b8"/>
        <stop offset="1" stop-color="#8e6a46"/>
      </radialGradient>
      <radialGradient id="roomLight" cx=".5" cy=".5" r=".6">
        <stop offset="0" stop-color="#f1ece4"/>
        <stop offset="1" stop-color="#a89a86"/>
      </radialGradient>
      <linearGradient id="agentTone" x1="0" y1="0" x2="0" y2="1">
        <stop offset="0" stop-color="#e3cc93"/>
        <stop offset=".35" stop-color="#c7a57f"/>
        <stop offset="1" stop-color="#1e2230"/>
      </linearGradient>
      <radialGradient id="portraitTone" cx=".5" cy=".45" r=".6">
        <stop offset="0" stop-color="#e8d2a4"/>
        <stop offset=".6" stop-color="#9fb6c6"/>
        <stop offset="1" stop-color="#2a3040"/>
      </radialGradient>
    </defs>

    <rect x="0" y="0" width="423" height="548" fill="url(#goldPanel)"/>
    <rect x="423" y="0" width="424" height="548" fill="var(--paper)"/>

    <path role="img" aria-label="Large exterior photo of the featured home" fill="url(#exteriorTone)"
      d="M58,0 L542,0 C640,55 740,120 847,149 L847,400 C720,425 560,412 440,395 C360,385 290,360 230,315 C150,255 90,140 58,0 Z"/>

    <path fill="var(--gold)" d="M520,0 C625,62 735,128 847,160 L847,0 Z"/>
    <path fill="var(--paper)" d="M560,0 C652,55 752,112 847,140 L847,0 Z"/>

    <path fill="var(--ink)" d="M30,0 L58,0 C90,140 150,255 230,315 C150,262 68,150 30,0 Z"/>
    <path fill="var(--ink)" d="M230,315 C290,360 360,385 440,395 C560,412 720,425 847,400 L847,414 C700,445 560,442 440,424 C350,410 280,372 230,315 Z"/>

    <g class="room-thumbs">
      <circle cx="80" cy="110" r="58" fill="#fff"/>
      <circle role="img" aria-label="Bathroom photo" cx="80" cy="110" r="53" fill="url(#roomWarm)"/>
      <circle cx="150" cy="201" r="58" fill="#fff"/>
      <circle role="img" aria-label="Living room photo" cx="150" cy="201" r="53" fill="url(#roomLight)"/>
      <circle cx="235" cy="285" r="58" fill="#fff"/>
      <circle role="img" aria-label="Staircase and lounge photo" cx="235" cy="285" r="53" fill="url(#roomWarm)"/>
      <circle cx="340" cy="343" r="58" fill="#fff"/>
      <circle role="img" aria-label="Kitchen photo" cx="340" cy="343" r="53" fill="url(#roomLight)"/>
    </g>

    <path role="img" aria-label="Full-length photo of the broker" fill="url(#agentTone)" opacity=".9"
      d="M20,548 L20,420 C20,330 45,290 80,278 C110,272 135,300 140,340 C150,390 175,420 190,450 L214,548 Z"/>

    <path fill="var(--ink)" d="M119,462 L228,462 L243,487 L228,513 L119,513 Z"/>

    <circle cx="768" cy="401" r="57" fill="#fff"/>
    <circle role="img" aria-label="Portrait of the broker" cx="768" cy="401" r="52" fill="url(#portraitTone)"/>
  </svg>

  <div class="fold"></div>

  <div class="abs team-tag">
    <span class="team-tag__name">PELHAM GROUP</span>
    <span class="team-tag__sub">Real Estate</span>
  </div>

  <div class="abs agent-card agent-card--back">
    <div class="agent-card__name">Maelle Hutchins</div>
    <div class="agent-card__title">Real Estate Broker</div>
    <div class="agent-card__phone">206.555.0174</div>
    <div class="agent-card__email">maelle.hutchin@norvalehomes.com</div>
  </div>

  <div class="abs brand brand--front">Norvale Homes</div>

  <div class="abs front-desc">
    <h2 class="heading-block">Property<br>Description</h2>
    <p>Beatur aligniatur aut eos utem hillaut dunducia comnis qui sundeRo odi doluptur? Itatem qui dolut ut ut qui ipsumquati tempori tatiae pre sint velecea simpor</p>
  </div>

  <div class="abs agent-card agent-card--front">
    <div class="agent-card__name">Maelle Hutchins</div>
    <div class="agent-card__title">Real Estate Broker</div>
    <div class="agent-card__phone">206.555.0174</div>
    <div class="agent-card__email">maelle.hutchin@norvalehomes.com</div>
  </div>
</section>

<!-- Inside spread -->
<section class="spread spread--inside">
  <svg class="art" viewBox="0 0 847 548">
    <defs>
      <linearGradient id="interiorTone" x1="0" y1="0" x2="1" y2="0">
        <stop offset="0" stop-color="#8a7a5c"/>
        <stop offset=".45" stop-color="#e7e0cf"/>
        <stop offset="1" stop-color="#b39a5a"/>
      </linearGradient>
      <radialGradient id="thumbWarm" cx=".5" cy=".5" r=".6">
        <stop offset="0" stop-color="#e9d6b9"/>
        <stop offset="1" stop-color="#8a6843"/>
      </radialGradient>
      <radialGradient id="thumbCool" cx=".5" cy=".5" r=".6">
        <stop offset="0" stop-color="#d5d9c4"/>
        <stop offset="1" stop-color="#8a7350"/>
      </radialGradient>
      <radialGradient id="thumbShadow" cx=".5" cy=".5" r=".5">
        <stop offset="0" stop-color="#000" stop-opacity=".28"/>
        <stop offset="1" stop-color="#000" stop-opacity="0"/>
      </radialGradient>
    </defs>

    <path fill="var(--ink)" d="M0,0 H847 V290 C740,300 600,305 470,335 L0,345 Z"/>

    <path fill="var(--gold)" d="M560,0 C652,60 742,105 847,124 V0 Z"/>
    <path fill="var(--paper)" d="M582,0 C662,50 752,92 847,106 V0 Z"/>

    <path fill="var(--gold)" d="M0,160 C150,132 310,170 470,256 L470,270 C310,186 150,148 0,175 Z"/>
    <path role="img" aria-label="Wide interior photo of the living room" fill="url(#interiorTone)"
      d="M0,175 C150,148 310,186 470,270 L470,322 C300,322 150,330 0,340 Z"/>
    <path fill="var(--gold)" d="M0,340 C150,330 300,322 470,322 L470,334 C300,336 150,345 0,360 Z"/>
    <path fill="var(--paper)" d="M0,360 C150,345 300,336 470,334 C600,305 740,300 847,290 V548 H0 Z"/>

    <g class="room-thumbs">
      <ellipse cx="500" cy="366" rx="56" ry="7" fill="url(#thumbShadow)"/>
      <ellipse cx="629" cy="366" rx="56" ry="7" fill="url(#thumbShadow)"/>
      <ellipse cx="760" cy="366" rx="56" ry="7" fill="url(#thumbShadow)"/>
      <circle cx="500" cy="295" r="62" fill="#fff"/>
      <circle role="img" aria-label="Staircase and lounge photo" cx="500" cy="295" r="57" fill="url(#thumbWarm)"/>
      <circle cx="629" cy="295" r="62" fill="#fff"/>
      <circle role="img" aria-label="Family room photo" cx="629" cy="295" r="57" fill="url(#thumbCool)"/>
      <circle cx="760" cy="295" r="62" fill="#fff"/>
      <circle role="img" aria-label="Master bathroom photo" cx="760" cy="295" r="57" fill="url(#thumbWarm)"/>
    </g>
  </svg>

  <div class="fold"></div>

  <h1 class="abs page-head">Page Head<br>Will Go Here</h1>
  <p class="abs page-intro">Beatur aligniatur aut eos utem hillaut dunducia comnis qui sundeRo odi doluptur? Itatem qui dolut ut ut qui ipsumquati tempori tatiae pre sint velecea simpor</p>
  <p class="abs side-column">Omniscid ucitassit dolorru mendeni hicidenderum quaepudis receaquiae vel idellup tatquis autem et harit, ut excest, cumqui se preribus rehent aut placcae inis maxima quis nis dolupic turiam aut illendit etur, sit omnis moluptatquam quide et vendigenimi, coribus si dolorit mi, comnimusam rempor aut ate nus, tem ullaut reptas non conecer ovition seriate volorrorumet vollabo. Ibus ad maio venduci aut fugit quate volorat mod qui dente es nostrum undam rem que pro ma sum quia soluptate</p>

  <h2 class="abs subhead">Subhead</h2>
  <p class="abs subhead-intro">Beatur aligniatur aut eos utem hillaut dunducia comnis qui sundeRo odi doluptur? Itatem qui dolut ut ut qui ipsumquati tempori tatiae pre sint velecea simpor</p>
  <p class="abs body-column body-column--one">Omniscid ucitassit dolorru mendeni hicidenderum quaepudis receaquiae vel idellup tatquis autem et harit, ut excest, cumqui se preribus rehent aut placcae inis maxima quis nis dolupic turiam aut illendit etur, sit omnis moluptatquam quide et vendigenimi, coribus si dolorit mi, comnimusam rempor aut ate nus, tem ullaut reptas non conecer ovition seriate volorrorumet vollabo. Ibus ad maio venduci aut fugit quate volorat mod qui dente es nostrum</p>
  <p class="abs body-column body-column--two">Omniscid ucitassit dolorru mendeni hicidenderum quaepudis receaquiae vel idellup tatquis autem et harit, ut excest, cumqui se preribus rehent aut placcae inis maxima quis nis dolupic turiam aut illendit etur, sit omnis moluptatquam quide et vendigenimi, coribus si dolorit mi, comnimusam rempor aut ate nus, tem ullaut reptas non conecer ovition seriate volorrorumet vollabo. Ibus ad maio venduci aut fugit quate volorat mod qui dente es nostrum</p>

  <h2 class="abs bullets-head">Bullet<br>Points Head</h2>
  <ul class="abs bullet-list">
    <li>Tem ellabor emolupid qui restiaes velese</li>
    <li>volum sim qui alita dolupta culluptae consequunte nobitem porectur?</li>
    <li>Ilianda erferia spicimp erferis event la dolendem et am</li>
    <li>quid quia dolorpo remqui ut ommoluptatio excero con porehen dandeliti aut et</li>
  </ul>
  <div class="abs brand brand--inside">Norvale Homes</div>
  <p class="abs side-note">Omniscid ucitassit dolorru mendeni hicidenderum quaepudis receaquiae vel idellup tatquis autem et harit, ut excest, cumqui se preribus rehent aut placcae inis maxima quis nis dolupic turiam aut illendit etur, sit omnis moluptatquam quide et vendigenimi, coribus si dolorit mi, comnimusam rempor aut ate nus, tem ullaut reptas non conecer</p>

  <div class="abs listing listing--one">
    <h3 class="heading-block">Property<br>Description</h3>
    <p>Omniscid ucitassit dolorru mendeni hicidenderum quaepudis receaquiae vel idellup tatquis autem et harit, ut excest, cumqui se preribus rehent aut placcae inis maxima quis nis dolupic turiam aut illendit etur, sit omnis moluptatquam quide et vendigenimi, coribus si dolorit</p>
  </div>
  <div class="abs listing listing--two">
    <h3 class="heading-block">Property<br>Description</h3>
    <p>Omniscid ucitassit dolorru mendeni hicidenderum quaepudis receaquiae vel idellup tatquis autem et harit, ut excest, cumqui se preribus rehent aut placcae inis maxima quis nis dolupic turiam aut illendit etur, sit omnis moluptatquam quide et vendigenimi, coribus si dolorit mi, comnimusam rempor aut</p>
  </div>
  <div class="abs listing listing--three">
    <h3 class="heading-block">Property<br>Description</h3>
    <p>Omniscid ucitassit dolorru mendeni hicidenderum quaepudis receaquiae vel idellup tatquis autem et harit, ut excest, cumqui se preribus rehent aut placcae inis maxima quis nis dolupic turiam aut illendit etur, sit omnis moluptatquam quide et vendigenimi, coribus si dolorit mi, comnimusam rempor aut</p>
  </div>
</section>

</body>
</html>
```